Redesign of key pages of website

We have a website in development: (You can see the test version here: https://staging.pawvira.ai) We want a redesign of a) the home page, b) the set up screens (all four steps), c) the account home page, and the chat page (all four linked below). It needs to look amazing in both desktop and mobile. Also, the chat page needs to have a few different versions to give people a choice between them.

Four areas:
1) Home page: https://staging.pawvira.ai/
2) Account pages: https://staging.pawvira.ai/account/chatsettings.php?step=1
3) Account home page (you'll need to set up an account which is free): https://staging.pawvira.ai/account/summary.php
4) Chat page: https://staging.pawvira.ai/chat.php?id=375

Also to clarify re: code, I don't need any of the interaction/behavior code. I just need the basic HTML and stylesheets so I can integrate that into the existing website.

Please feel free to pass by early versions to me or if you have any clarifications, let me know!

Industry/Entity Type

small businesses

Coding

Coded - Design and coding required

Number of Pages Required

5+ page

Font styles to use
Other font styles liked:
• keep the current font.

Requirements
Must have
• All the same elements/functionality on the current site. Just want a redesign. Also keep the dog visual. Also must work great in mobile and desktop and be really fun and modern and easy.
Nice to have
• Also in the setup pages, need a much better form of navigation (currently just have four circles.)

```html
<!DOCTYPE html>
<html lang="en">
<head>
<meta charset="utf-8">
<title>Pawvira — Your lead assistant</title>
<link href="https://fonts.googleapis.com/css2?family=Quicksand:wght@500;600;700&family=Nunito:wght@400;600;700&display=swap" rel="stylesheet">
<style>
:root{
  --blue:#4b86f5;
  --blue-soft:#e6efff;
  --blue-pale:#f2f6ff;
  --coral:#f27a78;
  --ink:#1d1f2b;
  --muted:#4a4d5c;
  --line:#d9e3f5;
  --navy:#0a0f2c;
  --white:#ffffff;
}
*{box-sizing:border-box;margin:0;padding:0}
html,body{width:1200px;height:4172px;overflow:hidden}
body{position:relative;background:var(--white);font-family:"Nunito",sans-serif;color:var(--ink)}
.abs{position:absolute}
.head{font-family:"Quicksand",sans-serif;font-weight:700}

/* header */
.brand{left:160px;top:50px;display:flex;align-items:center;gap:12px;font-family:"Quicksand",sans-serif;font-weight:700;font-size:38px;color:var(--ink)}
.brand-dot{width:16px;height:16px;border-radius:50%;background:var(--blue)}
.btn{display:flex;align-items:center;justify-content:center;border-radius:8px;color:#fff;font-size:16px;font-weight:600}
.btn-register{left:752px;top:56px;width:136px;height:44px;background:var(--blue)}
.btn-login{left:904px;top:56px;width:136px;height:44px;background:var(--coral)}

/* hero */
.hero-glow{left:300px;top:380px;width:600px;height:600px;border-radius:50%;background:radial-gradient(circle,rgba(120,160,255,.18),rgba(255,255,255,0) 70%)}
.eyebrow{left:0;width:1200px;top:178px;text-align:center;font-size:18px;font-weight:700;letter-spacing:1px}
.eyebrow::before{content:"";display:inline-block;width:40px;height:2px;background:var(--ink);vertical-align:middle;margin-right:14px}
.hero-title{left:0;width:1200px;top:212px;text-align:center;font-size:36px;line-height:44px}
.btn-create{left:540px;top:336px;width:160px;height:44px;background:var(--blue);font-size:14px}
.example-link{left:0;width:1200px;top:400px;text-align:center;font-size:13px;text-decoration:underline}
.mascot{background:radial-gradient(ellipse at 45% 45%,#c9d6ff,#8fb0fb 55%,#4b86f5 100%);border-radius:46% 46% 40% 40%}
.mascot-hero{left:400px;top:450px;width:340px;height:430px}
.hello-bubble{left:240px;top:856px;width:124px;height:34px;border-radius:8px;background:var(--blue-pale);font-size:12px;display:flex;align-items:center;justify-content:center;box-shadow:0 4px 12px rgba(60,90,160,.15)}

/* customize */
.customize-title{left:120px;top:1040px;font-size:32px;line-height:40px}
.divider{left:388px;top:1020px;width:2px;height:120px;background:var(--line)}
.customize-text{left:440px;top:1036px;width:640px;font-size:18px;line-height:30px;color:var(--muted)}

/* chat card */
.chat-card{left:240px;top:1264px;width:720px;height:536px;border-radius:24px;background:var(--white);box-shadow:0 0 0 14px var(--blue-soft),0 20px 50px rgba(75,134,245,.18);overflow:hidden}
.chat-avatar{left:-30px;top:20px;width:140px;height:140px;border-radius:50%;border:4px solid #f2a460;background:#fff5ec}
.chat-name{left:200px;top:50px;font-size:34px;color:var(--blue)}
.chat-role{left:200px;top:94px;font-size:20px;color:var(--blue)}
.social-row{left:200px;top:136px;display:flex;gap:22px}
.social-row span{width:38px;height:38px;border-radius:50%;background:var(--ink)}
.chat-mascot{left:40px;top:250px;width:150px;height:150px}
.chat-msg{left:230px;top:260px;width:440px;font-size:28px;line-height:40px;color:var(--ink)}
.chat-input{left:0;top:440px;width:720px;height:96px;background:var(--blue-pale);border-top:1px solid var(--line)}
.chat-placeholder{left:24px;top:470px;font-size:24px;color:#8b90a3}
.send-btn{left:620px;top:450px;width:76px;height:76px;border-radius:50%;background:var(--coral);display:flex;align-items:center;justify-content:center}

/* section titles */
.sec-title{left:0;width:1200px;text-align:center;font-size:36px}
.sec-text{left:280px;width:640px;text-align:center;font-size:20px;line-height:32px;color:var(--ink)}

/* calendar */
.cal-card{left:250px;top:2160px;width:710px;height:380px;border-radius:24px;background:#fff;box-shadow:0 0 0 14px var(--blue-soft),0 20px 50px rgba(75,134,245,.15)}
.cal-label{left:40px;top:40px;font-size:20px;font-weight:700;line-height:26px}
.cal-month{left:330px;top:46px;display:flex;gap:40px;font-size:20px;font-weight:700}
.cal-month .arrow{color:var(--muted)}
.cal-grid{left:36px;top:152px;width:424px;display:grid;grid-template-columns:repeat(7,1fr);row-gap:20px;text-align:center;font-size:17px;color:var(--muted)}
.cal-grid .dow{background:var(--blue);color:#fff;font-weight:700;padding:6px 0}
.cal-grid .sel{background:var(--blue);color:#fff;border-radius:6px;margin:0 8px}
.cal-sep{left:478px;top:140px;width:2px;height:190px;background:var(--line)}
.slots{left:500px;top:120px;display:flex;flex-direction:column;gap:20px}
.slot{width:170px;height:50px;border:2px solid var(--line);border-radius:8px;display:flex;align-items:center;justify-content:center;color:var(--blue);font-weight:700;font-size:18px}

/* leads table */
.leads-card{left:240px;top:2930px;width:720px;height:400px;border-radius:24px;background:var(--blue-pale)}
.leads-table{left:36px;top:50px;width:648px;border-collapse:separate;border-spacing:0 10px;font-size:13px}
.leads-table th{background:var(--blue);color:#fff;text-align:left;padding:6px 16px;font-size:16px}
.leads-table td{background:#fff;padding:14px 16px;vertical-align:middle;box-shadow:0 2px 8px rgba(60,90,160,.08)}
.leads-table ul{padding-left:18px;line-height:20px}
.leads-table td.email{font-size:14px;border-left:10px solid var(--blue-pale)}

/* cta */
.cta-band{left:160px;top:3490px;width:880px;height:210px;border-radius:24px;background:linear-gradient(90deg,#eef1f7,#f7f8fb)}
.cta-title{left:250px;top:3530px;font-size:36px;line-height:46px}
.btn-cta{left:250px;top:3632px;width:176px;height:44px;background:var(--coral);font-size:14px}
.mascot-cta{left:680px;top:3440px;width:230px;height:280px}

/* footer */
.footer{left:0;top:3870px;width:1200px;height:302px;background:var(--navy);color:#fff}
.footer-brand{left:160px;top:70px;display:flex;align-items:center;gap:12px;font-family:"Quicksand",sans-serif;font-weight:700;font-size:38px}
.footer-social{left:160px;top:130px;display:flex;gap:18px}
.footer-social span{width:22px;height:22px;border-radius:50%;background:var(--blue)}
.connect{left:800px;top:70px;width:240px;text-align:right;font-family:"Quicksand",sans-serif;font-weight:700;font-size:44px;line-height:46px}
.footer-rule{left:160px;top:236px;width:880px;height:1px;background:rgba(255,255,255,.2)}
.copyright{left:160px;top:254px;font-size:14px}
.legal{left:740px;top:254px;width:300px;text-align:right;font-size:14px}
</style>
</head>
<body>

<header>
  <div class="abs brand"><span class="brand-dot"></span>Pawvira</div>
  <a class="abs btn btn-register">Register</a>
  <a class="abs btn btn-login">Login</a>
</header>

<section class="hero">
  <div class="abs hero-glow"></div>
  <p class="abs eyebrow">WELCOME</p>
  <h1 class="abs hero-title head">Vira talks to your leads, qualifies them,<br>and gets them on your calendar.</h1>
  <a class="abs btn btn-create">Create Your Vira Now</a>
  <a class="abs example-link">See An Example!</a>
  <div class="abs mascot mascot-hero" role="img" aria-label="Blue and white cartoon dog mascot sitting"></div>
  <div class="abs hello-bubble">Hi, Vira Here!</div>
</section>

<section class="customize">
  <h2 class="abs customize-title head">Customize<br>&amp; Share</h2>
  <div class="abs divider"></div>
  <p class="abs customize-text">Customize the appearance, conversation, and much more. You can then share Vira by embedding it in your website or via a personalized link.</p>
</section>

<section class="abs chat-card">
  <div class="abs chat-avatar"></div>
  <div class="abs chat-name head">Mara Salon</div>
  <div class="abs chat-role">Hairdresser/Stylist</div>
  <div class="abs social-row"><span></span><span></span><span></span><span></span></div>
  <div class="abs mascot chat-mascot" role="img" aria-label="Small dog mascot avatar"></div>
  <p class="abs chat-msg">Hi! I'm Vira, Mara's assistant. How did you hear about Mara?</p>
  <div class="abs chat-input"></div>
  <div class="abs chat-placeholder">Enter your message...</div>
  <div class="abs send-btn">
    <svg width="34" height="34" viewBox="0 0 24 24" fill="none" stroke="#fff" stroke-width="2" stroke-linejoin="round"><path d="M22 2 11 13"/><path d="M22 2 15 22l-4-9-9-4z"/></svg>
  </div>
</section>

<section class="schedule">
  <h2 class="abs sec-title head" style="top:1900px">Qualify &amp; Schedule</h2>
  <p class="abs sec-text" style="top:1968px">Get the information you need from your customers. After they meet your criteria, they can book a meeting directly on your calendar.</p>
  <div class="abs cal-card">
    <div class="abs cal-label">Select A<br>Date &amp; Time</div>
    <div class="abs cal-month"><span class="arrow">←</span><span>June 2023</span><span class="arrow">→</span></div>
    <div class="abs cal-grid">
      <div class="dow">Sun</div><div class="dow">Mon</div><div class="dow">Tue</div><div class="dow">Wed</div><div class="dow">Thu</div><div class="dow">Fri</div><div class="dow">Sat</div>
      <div></div><div></div><div></div><div></div><div>01</div><div>02</div><div>03</div>
      <div>04</div><div>05</div><div>06</div><div class="sel">07</div><div>08</div><div>09</div><div>10</div>
      <div>11</div><div>12</div><div>13</div><div>14</div><div>15</div><div>16</div><div>17</div>
    </div>
    <div class="abs cal-sep"></div>
    <div class="abs slots"><div class="slot">10:00 AM</div><div class="slot">10:00 AM</div><div class="slot">10:00 AM</div></div>
  </div>
</section>

<section class="leads">
  <h2 class="abs sec-title head" style="top:2668px">Manage Your leads</h2>
  <p class="abs sec-text" style="top:2740px">Get notified via email or text. See a summary of each lead and manage them in one place. Search, sort, add notes, and more.</p>
  <div class="abs leads-card">
    <table class="abs leads-table">
      <thead><tr><th style="width:62%">Summary</th><th>Email</th></tr></thead>
      <tbody>
        <tr><td><ul><li>Interested in a fitness coach</li><li>Does not currently work out</li><li>Specifically interested in arms and strength</li><li>In the Seattle area and flexible on time</li></ul></td><td class="email">jonahwells@inboxly.com</td></tr>
        <tr><td><ul><li>Interested in a new fitness coach</li><li>Works out 3 times a week</li><li>Has a fitness instructor now but his approach is too relaxed</li></ul></td><td class="email">priyamarsh@inboxly.com</td></tr>
      </tbody>
    </table>
  </div>
</section>

<section class="cta">
  <div class="abs cta-band"></div>
  <h2 class="abs cta-title head">Let Vira Handle<br>Your Leads Today!</h2>
  <a class="abs btn btn-cta">Create Your Vira Now</a>
  <div class="abs mascot mascot-cta" role="img" aria-label="Blue and white cartoon dog mascot"></div>
</section>

<footer class="abs footer">
  <div class="abs footer-brand"><span class="brand-dot"></span>Pawvira</div>
  <div class="abs footer-social"><span></span><span></span><span></span><span></span></div>
  <div class="abs connect">↗ LET'S<br>CONNECT!</div>
  <div class="abs footer-rule"></div>
  <p class="abs copyright">© 2023 Pawvira. All rights reserved.</p>
  <p class="abs legal">Terms &amp; Conditions &nbsp;|&nbsp; Privacy Policy</p>
</footer>

</body>
</html>
```